my website is tabellepiece.com. (brand name is ta belle pièce) This is just a template that i have choose for. The content and the pictures are not about my business just the template.
I would like to have 4 pages for now. 1 homepage, which will be an overview for all pages, it is right now in this way. It will directly highlight my story. My website will tell an exclusive story about details which makes the difference and will make people happy with very small things. It will be art related but very stylish as well. I also want to have a event agenda on my homepage where people can see where my next event is. Page 2 my blog, where I will write weekly about mindset, lifestyle and details. Inspiration place for people who are looking for unique and exclusive approaches in life. Page 3 shop, where I will sell my stuff which is handmade and unique, it will be limited edition stuff. Mostly I will make the designs from marbling art, which I am a teacher for. (https://www.vidorastream.com/watch?v=Kq7TbWm2Xa) check this video out for more. Page 4 is book page. Here people will be able to book private or group classes for marbling art (check the video). I have already a community of more than 500 people on join ring, which will be my public as well. I wanna implement the join ring button on this page as well. to be able to track.

This is about my website. I also need a logo for my brand, which will suit my website and my goals.

I can also give you a reference website, which really like as structure and style;
https://www.brightmorrowco.com/products/the-daybook-organizer?ref=Xp4RtLm8QzVw2NbKc7HsJd9FgTy3MvEqBa6WnUoZr1LkPxYhGiCe5DsAtQfVbNj0HmRwKyXo8LcTpZaEsUv2GqDnIwMb

ta belle pièce

4 page

• I can also give you a reference website, which really like as structure and style;
• https://www.brightmorrowco.com/products/the-daybook-organizer?ref=Xp4RtLm8QzVw2NbKc7HsJd9FgTy3MvEqBa6WnUoZr1LkPxYhGiCe5DsAtQfVbNj0HmRwKyXo8LcTpZaEsUv2GqDnIwMb

```html
<!DOCTYPE html>
<html lang="en">
<head>
<meta charset="utf-8">
<title>ta belle pièce</title>
<link href="https://fonts.googleapis.com/css2?family=Montserrat:wght@400;500;600&family=Lato:wght@400&display=swap" rel="stylesheet">
<style>
  :root {
    --paper: #ffffff;
    --ink: #1a1a1a;
    --band: #232323;
    --muted: #7a7a7a;
    --body-text: #5f5f5f;
    --line: #2a2a2a;
  }
  html, body {
    margin: 0;
    padding: 0;
    width: 1200px;
    height: 1200px;
    overflow: hidden;
    background: var(--paper);
  }
  .page {
    position: relative;
    width: 1200px;
    height: 1200px;
    overflow: hidden;
    font-family: "Montserrat", sans-serif;
    color: var(--ink);
  }
  .gallery-tile {
    position: absolute;
    top: 12px;
    width: 277px;
    height: 278px;
  }
  .tile-1 { left: 162px; background: linear-gradient(170deg, #8a7a6a 0%, #3a3530 30%, #1f1f1f 70%, #9a9590 100%); }
  .tile-2 { left: 462px; background: linear-gradient(175deg, #8a2a30 0%, #b7a89a 22%, #8fc6c4 45%, #6e8a3c 70%, #a8cfc8 100%); }
  .tile-3 { left: 762px; background: linear-gradient(170deg, #8a7a6a 0%, #3a3530 30%, #1f1f1f 70%, #9a9590 100%); }

  .see-more {
    position: absolute;
    left: 536px;
    top: 350px;
    width: 128px;
    height: 38px;
    box-sizing: border-box;
    border: 1px solid var(--line);
    display: flex;
    align-items: center;
    justify-content: center;
    font-size: 10.5px;
    font-weight: 500;
    letter-spacing: 0.5px;
    color: var(--ink);
    text-decoration: none;
  }

  .testimonial {
    position: absolute;
    left: 0;
    top: 446px;
    width: 1200px;
    height: 301px;
    background: var(--band);
    color: var(--paper);
    text-align: center;
  }
  .quote-badge {
    position: absolute;
    left: 577px;
    top: 62px;
    width: 44px;
    height: 44px;
  }
  .quote-text {
    position: absolute;
    left: 0;
    width: 1200px;
    top: 162px;
    margin: 0;
    font-size: 13px;
    font-weight: 600;
    letter-spacing: 1.8px;
    line-height: 18.5px;
  }
  .quote-author {
    position: absolute;
    left: 0;
    width: 1200px;
    top: 227px;
    margin: 0;
    font-size: 10px;
    font-weight: 600;
    letter-spacing: 0.3px;
  }

  .about {
    position: absolute;
    left: 0;
    top: 798px;
    width: 1200px;
    text-align: center;
  }
  .about-title {
    margin: 0;
    font-size: 17.5px;
    font-weight: 500;
    letter-spacing: 0.8px;
    line-height: 28px;
  }
  .about-subtitle {
    margin: 4px 0 0;
    font-size: 10px;
    font-weight: 400;
    letter-spacing: 1px;
    color: var(--muted);
  }
  .about-rule {
    position: absolute;
    left: 536px;
    top: 61px;
    width: 128px;
    height: 1px;
    background: var(--line);
  }
  .about-copy {
    position: absolute;
    left: 0;
    top: 116px;
    width: 1200px;
    margin: 0;
    font-family: "Lato", sans-serif;
    font-size: 10.5px;
    letter-spacing: 0.9px;
    line-height: 18.8px;
    color: var(--body-text);
  }

  .team-portrait {
    position: absolute;
    top: 1027px;
    width: 203px;
    height: 180px;
  }
  .portrait-1 { left: 162px; background: linear-gradient(180deg, #c9c9c9 0%, #d8d8d8 100%); }
  .portrait-2 { left: 386px; background: linear-gradient(180deg, #6f7478 0%, #5d6a70 100%); }
  .portrait-3 { left: 611px; background: linear-gradient(180deg, #5a6068 0%, #4a4f56 100%); }
  .portrait-4 { left: 836px; background: linear-gradient(180deg, #b9a892 0%, #8a7a68 100%); }
</style>
</head>
<body>
<main class="page">
  <section class="gallery">
    <div class="gallery-tile tile-1" role="img" aria-label="Marbling tray with ink drops on dark water and paint jars"></div>
    <div class="gallery-tile tile-2" role="img" aria-label="Finished marbled paper with floral patterns in pink, green and blue"></div>
    <div class="gallery-tile tile-3" role="img" aria-label="Marbling tray with ink drops on dark water and paint jars"></div>
    <a class="see-more" href="#">SEE MORE</a>
  </section>

  <section class="testimonial">
    <svg class="quote-badge" viewBox="0 0 44 44" aria-hidden="true">
      <circle cx="22" cy="22" r="22" fill="#ffffff"/>
      <path d="M16.5 17.5c2 0 3.3 1.4 3.3 3.3 0 3-2.3 5.6-5.4 6.3l-.5-1.1c1.6-.7 2.6-1.8 2.8-3.1-1.7-.1-2.9-1.3-2.9-2.9 0-1.4 1.1-2.5 2.7-2.5zm8.4 0c2 0 3.3 1.4 3.3 3.3 0 3-2.3 5.6-5.4 6.3l-.5-1.1c1.6-.7 2.6-1.8 2.8-3.1-1.7-.1-2.9-1.3-2.9-2.9 0-1.4 1.1-2.5 2.7-2.5z" fill="#232323"/>
    </svg>
    <p class="quote-text">LOREM IPSUM DOLOR SIT, AD ETIAM SIT ONER<br>OL DEIAN BOST SIT EMIST.</p>
    <p class="quote-author">WREN CASTELLANE</p>
  </section>

  <section class="about">
    <h2 class="about-title">ABOUT US</h2>
    <p class="about-subtitle">WHO WE ARE</p>
    <div class="about-rule"></div>
    <p class="about-copy">Donec rutrum congue leo eget malesuada. Curabitur non nulla sit amet nisl tempus convallis<br>quis ac lectus. Sed porttitor lectus nibh. Proin eget tortor risus. Nulla porttitor accumsan tincidunt.<br>Nulla porttitor accumsan tincidunt.</p>
  </section>

  <section class="team">
    <div class="team-portrait portrait-1" role="img" aria-label="Team member portrait on light grey background"></div>
    <div class="team-portrait portrait-2" role="img" aria-label="Team member portrait on grey background"></div>
    <div class="team-portrait portrait-3" role="img" aria-label="Team member portrait on dark grey background"></div>
    <div class="team-portrait portrait-4" role="img" aria-label="Team member portrait outdoors in warm tones"></div>
  </section>
</main>
</body>
</html>
```